Corporate Business Card Design Project

..Hi designers!
I have established a consultancy within strategic communnications, for which I need a business card design - I've seen some of the things you do in here, and they're great! I'll provide some information in the following:
Name: BriarLedger
Tagline: Guiding Dialogue
Service: Strategic communications consulting (primariy internal communication and optimizing): various organisations - e.g. SMEs, NGOs and NPOs - are offered an analysis of their current efforts and, on the basis of that, management consulting tailored their unique challenges and needs.
It's a sole proprietorship - for now! - but it's my plan to employ 5-20 persons over the years. Therefore the card should NOT symbolize a start-up, but communicate a well-established, serious consultancy. Hence, it should also apply to serious companies and organizations - think Veltra or Hollis Brant Group (both as sender and receiver) ;)
The design should accordingly have a formal, conservative, stylish, corporate, clean look! and ditto colors, eg. black, grey, white etc - corresponding to the logo. The only colour that can appear is the same orange contrast as in my logo (see attachement). Not too bold or dramatic fonds or letters.
I choose the double sided as I think it gives the most professional look: One side with name, titel, phone, e-mail - then a little space - and four additional lines for address.
This composition is if all information should be in the same "column" - feel free to provide suggestions with the address places elsewhere on the one side.
On the other side, I'm only thinkin' something with the logo.
I'd be happy to see different ideas re. the use of the orange contrast, placement of logo, etc.
I do not plan on changing the design of businees cards ever - as I think it is more serious keeping a concept and avoid rebranding - and I'm sure that you can deliver an ever-lasting logo for my company! Thanks :).
Let's play the rest by ear in the correspondance.
Target Market(s)
Executive level: CEOs, HR directors, communication managers/directors, business owners.
Industry/Entity Type
Management Consulting

```html
<!DOCTYPE html>
<html lang="en">
<head>
<meta charset="utf-8">
<title>BriarLedger – Business Card</title>
<link rel="stylesheet" href="https://fonts.googleapis.com/css2?family=Open+Sans:wght@400;600&display=swap">
<style>
  :root {
    --page: #e9e7e4;
    --card-dark-1: #2a2a2a;
    --card-dark-2: #3b3b3b;
    --card-light: #ffffff;
    --orange: #f08a24;
    --ink: #1c1c1c;
    --ink-soft: #555555;
    --stripe-grey: #6d6d6d;
    --edge-grey: #cfd0d2;
  }
  * { margin: 0; padding: 0; box-sizing: border-box; }
  html, body {
    width: 1200px; height: 900px; overflow: hidden;
    background: var(--page);
    font-family: "Open Sans", Arial, sans-serif;
  }
  .canvas { position: relative; width: 1200px; height: 900px; }

  .card {
    position: absolute; left: 250px; width: 700px; height: 400px;
    box-shadow: 0 6px 18px rgba(0,0,0,0.18);
    overflow: hidden;
  }

  /* Back side */
  .card--back {
    top: 40px;
    background: linear-gradient(100deg, var(--card-dark-1) 0%, var(--card-dark-2) 55%, var(--card-dark-1) 100%);
  }
  .card--back .brand {
    position: absolute; left: 60px; top: 92px;
    color: #f2f2f2;
  }
  .brand__name { font-size: 40px; font-weight: 400; letter-spacing: 0.5px; line-height: 1; }
  .brand__tagline { font-size: 11px; letter-spacing: 2px; margin-top: 6px; color: #a9a9a9; }
  .stripes {
    position: absolute; height: 22px;
    background: repeating-linear-gradient(90deg, var(--stripe-grey) 0 2px, transparent 2px 6px);
  }
  .stripes--upper { left: 470px; top: 108px; width: 170px; }
  .stripes--lower { left: 40px; top: 222px; width: 210px; }
  .card--back .service {
    position: absolute; left: 265px; top: 220px;
    color: var(--orange); font-size: 20px; letter-spacing: 0.4px;
  }
  .card--back .base-band {
    position: absolute; left: 0; bottom: 0; width: 100%; height: 22px;
    background: var(--orange);
  }

  /* Front side */
  .card--front { top: 470px; background: var(--card-light); }
  .card--front .top-band {
    position: absolute; left: 0; top: 0; width: 100%; height: 30px;
    background: repeating-linear-gradient(90deg, var(--orange) 0 2px, #ffffff 2px 5px);
  }
  .card--front .brand {
    position: absolute; left: 55px; top: 120px; color: var(--ink);
  }
  .card--front .brand__tagline { color: var(--ink-soft); }
  .contact {
    position: absolute; left: 425px; top: 120px;
    color: var(--ink); font-size: 13px; line-height: 1.5;
  }
  .contact__name { font-size: 15px; }
  .contact__role { font-size: 15px; margin: 4px 0 14px 14px; }
  .contact__line { color: var(--ink-soft); margin-left: 28px; margin-bottom: 6px; }
  .card--front .base-edge {
    position: absolute; left: 0; bottom: 0; width: 100%; height: 14px;
    background: linear-gradient(180deg, #e4e5e6, var(--edge-grey));
  }
</style>
</head>
<body>
<main class="canvas">

  <section class="card card--back" aria-label="Business card, back">
    <div class="brand">
      <div class="brand__name">BriarLedger</div>
      <div class="brand__tagline">Guiding Dialogue</div>
    </div>
    <div class="stripes stripes--upper"></div>
    <div class="stripes stripes--lower"></div>
    <p class="service">Strategic communications consulting</p>
    <div class="base-band"></div>
  </section>

  <section class="card card--front" aria-label="Business card, front">
    <div class="top-band"></div>
    <div class="brand">
      <div class="brand__name">BriarLedger</div>
      <div class="brand__tagline">Guiding Dialogue</div>
    </div>
    <div class="contact">
      <p class="contact__name">Dr. Name Surmname</p>
      <p class="contact__role">Position</p>
      <p class="contact__line">Office phone: 555-014-2270</p>
      <p class="contact__line">After Hour number 555-014-8836</p>
      <p class="contact__line">Office address 2210</p>
      <p class="contact__line">Alder Rd. Westfield Ks 60000</p>
    </div>
    <div class="base-edge"></div>
  </section>

</main>
</body>
</html>
```